Need modern simple design for magazine ad, apartment and condo roofer.

I need a half page magazine ad for a local roofer to publish in an industry magazine. Apartment associations industry. All types of roofs. Shingle and Flat
Need the design to be creative and modern, clean and simple. I do not want a busy design. One that stands out and makes a point quickly.
Logo must be prominent.
DO NOT USE PHOTOS FROM MY WEBSITE PLEASE. Looking for something new.
I work on entire complexes not houses.

Need to make sure our phone number and email address are listed at the bottom. Here is my website www.vorbelan.com
Want to stay away from standard clip arts of tools, homes, apartment buildings.
Half Horizontal 7.25 x 4.75
Ads should be in PDF and JPG format.

Target Market(s)

Apartment or Condo owners looking for large scale roofing projects

Industry/Entity Type

Roofing

Requirements
Must have
• Prominent Logo
Simple Clean Design
Create graphics
Not Busy
Should not have
• Clip Art
No Photos from my website

```html
<!DOCTYPE html>
<html lang="en">
<head>
<meta charset="utf-8">
<title>Vorbelan Roofing – Half Page Ad</title>
<link rel="stylesheet" href="https://fonts.googleapis.com/css2?family=Fira+Sans+Extra+Condensed:wght@400;500;600&family=Roboto:wght@900&display=swap">
<style>
  :root {
    --sky-light: #e9f1f8;
    --sky-mid: #7fb2dc;
    --roof-dark: #050607;
    --panel-blue: #2470c2;
    --panel-blue-low: #3d78c4;
    --band-blue: #2353a0;
    --accent-cyan: #00b0ea;
    --accent-soft: #5ec8f0;
    --white: #ffffff;
    --black: #000000;
  }
  * { margin: 0; padding: 0; box-sizing: border-box; }
  html, body { width: 1200px; height: 783px; overflow: hidden; background: var(--white); }
  .ad {
    position: relative;
    width: 1200px;
    height: 783px;
    overflow: hidden;
    font-family: "Fira Sans Extra Condensed", "Arial Narrow", sans-serif;
    color: var(--white);
  }
  .hero-photo {
    position: absolute; inset: 0;
    background:
      linear-gradient(162deg, transparent 0 52%, var(--roof-dark) 52.2%),
      linear-gradient(180deg, var(--sky-light) 0%, var(--sky-mid) 55%, #4f8fcc 100%);
  }
  .top-band {
    position: absolute; left: 373px; top: 0; width: 827px; height: 25px;
    background: linear-gradient(90deg, #6d86c0, var(--band-blue) 30%);
  }
  .brand-box {
    position: absolute; left: 33px; top: 0; width: 340px; height: 134px;
    background: var(--black);
    display: flex; align-items: center; justify-content: center; gap: 12px;
  }
  .brand-mark { width: 22px; height: 22px; background: var(--accent-cyan); }
  .brand-name { font-weight: 600; font-size: 40px; color: var(--white); letter-spacing: 0.5px; }
  .intro-panel {
    position: absolute; left: 33px; top: 134px; width: 340px; height: 570px;
    background: linear-gradient(180deg, var(--panel-blue) 0%, var(--panel-blue-low) 100%);
    opacity: 0.97;
  }
  .down-arrow-white { position: absolute; left: 184px; top: 124px; width: 38px; height: 66px; }
  .intro-copy {
    position: absolute; left: 48px; top: 190px; width: 310px;
    font-size: 22.5px; line-height: 27.6px; text-align: justify;
  }
  .intro-copy strong { font-weight: 600; }
  .intro-closer {
    position: absolute; left: 48px; top: 490px; width: 320px;
    font-size: 29px; line-height: 35px;
  }
  .down-arrow-cyan { position: absolute; left: 985px; top: 276px; width: 78px; height: 96px; }
  .tagline {
    position: absolute; right: 34px; top: 382px;
    text-align: right; color: var(--accent-cyan);
    font-weight: 500; font-size: 44px; line-height: 44px;
  }
  .headline-lead {
    position: absolute; left: 497px; top: 494px;
    color: var(--accent-soft); font-weight: 600; font-size: 48px;
  }
  .headline-main {
    position: absolute; left: 600px; top: 470px;
    font-family: "Roboto", "Arial Black", sans-serif;
    font-weight: 900; font-size: 132px; letter-spacing: -5px; line-height: 1;
  }
  .headline-note {
    position: absolute; left: 883px; top: 638px;
    font-size: 44px; font-weight: 500;
  }
  .contact-band {
    position: absolute; left: 0; top: 704px; width: 1200px; height: 79px;
    background: var(--band-blue);
    font-size: 24px;
  }
  .contact-item { position: absolute; top: 0; height: 79px; display: flex; align-items: center; gap: 10px; }
  .contact-item svg { fill: var(--white); }
  .contact-address { left: 114px; }
  .contact-phone { left: 663px; }
  .contact-email { left: 888px; }
  .contact-at { font-size: 28px; font-weight: 500; }
</style>
</head>
<body>
<div class="ad">
  <div class="hero-photo" role="img" aria-label="Photo of a roofer silhouetted against a bright blue sky, working on a dark sloped roof"></div>
  <div class="top-band"></div>

  <div class="intro-panel"></div>
  <div class="brand-box">
    <span class="brand-mark"></span>
    <span class="brand-name">Vorbelan Roofing</span>
  </div>

  <svg class="down-arrow-white" viewBox="0 0 38 66" aria-hidden="true">
    <path d="M8 0 H30 V42 H38 L19 66 L0 42 H8 Z" fill="#ffffff"/>
  </svg>

  <p class="intro-copy"><strong>VORBELAN ROOFING</strong>, has been improving and adding value to multifamily apartment communities and student housing developments for over 30 years now. Although we have done work in many other states, most of our projects are in the great state of Texas. From the simple to the lavish, we’ve experienced it all and we can help you every step of the way.</p>
  <p class="intro-closer">No job is too small or too big for our knowledgeable crews.</p>

  <svg class="down-arrow-cyan" viewBox="0 0 78 96" aria-hidden="true">
    <path d="M20 0 H58 V62 H78 L39 96 L0 62 H20 Z" fill="#00b0ea"/>
  </svg>

  <p class="tagline">We do work on entire<br>complexes not just houses</p>
  <p class="headline-lead">We do</p>
  <p class="headline-main">Roofing</p>
  <p class="headline-note">(all types)</p>

  <div class="contact-band">
    <div class="contact-item contact-address">
    <svg width="20" height="26" viewBox="0 0 20 26" aria-hidden="true"><path d="M10 0 A10 10 0 0 1 20 10 C20 17 10 26 10 26 C10 26 0 17 0 10 A10 10 0 0 1 10 0 Z M10 5 A5 5 0 1 0 10 15 A5 5 0 1 0 10 5 Z"/></svg>
      <span>412 Larkfield Avenue, Suite 210, Corvell, TX 75014</span>
    </div>
    <div class="contact-item contact-phone">
      <svg width="28" height="28" viewBox="0 0 24 24" aria-hidden="true"><path d="M6.6 10.8a15.1 15.1 0 0 0 6.6 6.6l2.2-2.2a1 1 0 0 1 1-.25 11.4 11.4 0 0 0 3.6.57 1 1 0 0 1 1 1V20a1 1 0 0 1-1 1A17 17 0 0 1 3 4a1 1 0 0 1 1-1h3.5a1 1 0 0 1 1 1c0 1.25.2 2.45.57 3.57a1 1 0 0 1-.25 1z"/></svg>
      <span>555.014.2290</span>
    </div>
    <div class="contact-item contact-email">
      <span class="contact-at">@</span>
      <span>info@vorbelan.com</span>
    </div>
  </div>
</div>
</body>
</html>
```